Business Card Re-Design for a Lighting Designer

I would like my business card re-designed. It is currently high gloss and they scratch too easily. I don not think the current design lends itself well to a matte finish. I have included the current design for reference along with our company logo.
Check out our website for current branding.
http://www.brambleorchidstudio.example

Updates
Some of the top contenders are muslim and it is a holiday for them. I do not want to discriminate and would expect the same courtesy for holidays we celebrate.
Target Market(s)
Interior Designers, Architects
Contact Information for Business Card
Logo - Name, Title, Address, Telephone Number and Extension, Email
Font styles to use
Requirements
Must have
- All the information listed on the current business card. If you use Red, it needs to be the red from our logo.
Nice to have
- Vertical and Horizontal Designs will be entertained.
Should not have
- Requirements for a glossy finish...should not look too corporate since we are a design firm.

```html
<!DOCTYPE html>
<html lang="en">
<head>
<meta charset="utf-8">
<title>Bramble Orchid Studio — Business Card</title>
<link href="https://fonts.googleapis.com/css2?family=Roboto+Condensed:wght@300;400;700&display=swap" rel="stylesheet">
<style>
  :root {
    --brand-red: #961b1e;
    --ink: #1f1f1f;
    --paper: #ffffff;
    --backdrop: #3a3b3b;
    --on-red: #ffffff;
  }
  * { box-sizing: border-box; margin: 0; padding: 0; }
  html, body {
    width: 1200px; height: 1200px; overflow: hidden;
    background: var(--backdrop);
    font-family: "Roboto Condensed", "Arial Narrow", sans-serif;
  }
  .sheet {
    width: 1200px; height: 1200px;
    display: flex; flex-direction: column; align-items: center; justify-content: center;
    gap: 40px;
  }
  .card {
    position: relative;
    width: 880px; height: 537px;
    background: var(--paper);
    overflow: hidden;
  }

  /* Front */
  .front-brand {
    position: absolute; left: 92px; top: 116px; width: 250px;
  }
  .brand-square {
    display: block; width: 130px; height: 130px;
    background: var(--brand-red);
    margin-bottom: 18px;
  }
  .brand-name {
    font-weight: 300; color: var(--ink);
    font-size: 42px; line-height: 44px; text-transform: uppercase;
  }
  .info-band {
    position: absolute; left: 372px; right: 0; top: 115px; height: 298px;
    background: var(--brand-red);
    color: var(--on-red);
    padding: 26px 0 0 34px;
  }
  .person-name {
    font-weight: 700; font-size: 32px; line-height: 34px; letter-spacing: 0.5px;
    text-transform: uppercase;
  }
  .person-title {
    font-weight: 700; font-size: 25px; line-height: 30px; letter-spacing: 2px;
    text-transform: uppercase; margin-bottom: 18px;
  }
  .contact-list { list-style: none; }
  .contact-list li {
    display: flex; align-items: flex-start;
    font-weight: 400; font-size: 25px; line-height: 31px;
  }
  .contact-icon {
    flex: 0 0 22px; width: 22px; height: 22px; margin: 5px 10px 0 0;
  }

  /* Back */
  .back-brand {
    position: absolute; left: 0; right: 0; top: 137px;
    display: flex; flex-direction: column; align-items: center;
  }
  .back-brand .brand-square { width: 96px; height: 96px; margin-bottom: 14px; }
  .back-brand .brand-name {
    color: var(--brand-red); font-size: 32px; line-height: 34px; text-align: center;
  }
  .web-address {
    position: absolute; left: 0; right: 0; top: 368px;
    text-align: center; color: var(--brand-red);
    font-weight: 400; font-size: 24px; letter-spacing: 3.5px;
  }
</style>
</head>
<body>
<main class="sheet">

  <section class="card card-front" aria-label="Card front">
    <div class="front-brand">
      <span class="brand-square"></span>
      <p class="brand-name">Bramble<br>Orchid<br>Studio</p>
    </div>

    <div class="info-band">
      <h1 class="person-name">Maren Holloway</h1>
      <p class="person-title">Principal</p>
      <ul class="contact-list">
        <li>
          <svg class="contact-icon" viewBox="0 0 22 22" aria-hidden="true">
            <circle cx="11" cy="11" r="11" fill="#fff"/>
            <path d="M11 4.5a4.5 4.5 0 0 0-4.5 4.5c0 3.2 4.5 8.5 4.5 8.5s4.5-5.3 4.5-8.5A4.5 4.5 0 0 0 11 4.5z" fill="#961b1e"/>
            <circle cx="11" cy="9" r="1.7" fill="#fff"/>
          </svg>
          <span>210 Fernwood Lane, Suite 14<br>Ashford, Georgia 30999 USA</span>
        </li>
        <li>
          <svg class="contact-icon" viewBox="0 0 22 22" aria-hidden="true">
            <circle cx="11" cy="11" r="11" fill="#fff"/>
            <rect x="5" y="7" width="12" height="8.5" rx="1" fill="#961b1e"/>
            <path d="M5.5 7.6 11 11.8l5.5-4.2" fill="none" stroke="#fff" stroke-width="1.2"/>
          </svg>
          <span>maren@brambleorchidstudio.example</span>
        </li>
        <li>
          <svg class="contact-icon" viewBox="0 0 22 22" aria-hidden="true">
            <circle cx="11" cy="11" r="11" fill="#fff"/>
            <path d="M7.3 5.2c.5-.4 1.1-.3 1.4.2l1.2 2c.3.5.2 1-.2 1.4l-.8.7c.6 1.4 1.7 2.6 3.1 3.3l.8-.8c.4-.4.9-.5 1.4-.2l2 1.2c.5.3.6.9.2 1.4l-1 1.2c-.5.6-1.3.8-2 .5-3.3-1.3-5.9-3.9-7.2-7.2-.3-.7-.1-1.5.5-2z" fill="#961b1e"/>
          </svg>
          <span>555 010 4420 x 1</span>
        </li>
        <li>
          <svg class="contact-icon" viewBox="0 0 22 22" aria-hidden="true">
            <circle cx="11" cy="11" r="11" fill="#fff"/>
            <circle cx="11" cy="11" r="6" fill="none" stroke="#961b1e" stroke-width="1.5"/>
            <ellipse cx="11" cy="11" rx="2.6" ry="6" fill="none" stroke="#961b1e" stroke-width="1.3"/>
            <path d="M5 11h12" stroke="#961b1e" stroke-width="1.3"/>
          </svg>
          <span>www.brambleorchidstudio.example</span>
        </li>
      </ul>
    </div>
  </section>

  <section class="card card-back" aria-label="Card back">
    <div class="back-brand">
      <span class="brand-square"></span>
      <p class="brand-name">Bramble<br>Orchid<br>Studio</p>
    </div>
    <p class="web-address">www.brambleorchidstudio.example</p>
  </section>

</main>
</body>
</html>
```